High-end construction company needs a business card design

We need a modern looking business card that draws people in, is memorable and looks so good people will want to sick it on their fridges.
On the first side what is needed are:
Logo
My name - Tomas Verbelk
Title - Managing Director
Website - www.kravel.co.uk
Email - tomas@kravel.co.uk
Telephone - 020 5194 6381
Mobile - 07845319027
On the back side was is needed is a list of all the services we provide:
-Kitchen Renovations
-Bathroom Renovations
-House Renovations
-Garage Conversions
-Extensions
-Loft Conversions
-Conservatories
-Carpentry
-Tiling
-Electrical
-Plumbing & Heating
-Bricklaying
-Landscaping
-Decorating
-Plastering
We would like the colours to be the same shades as on the logo with grey or black for the words.
Target Market(s)
Anyone who needs building work done
Contact Information for Business Card
This business card is for a construction company which strives to deliver excellent service and quality.
The look and feel of the card should represent this.
Requirements
Must have
- On the first side what is needed are:
Logo
My name - Tomas Verbelk
Title - Managing Director
Website - www.kravel.co.uk
Email - tomas@kravel.co.uk
Telephone - 020 5194 6381
Mobile - 07845319027
Nice to have
- Cool looking features

```html
<!DOCTYPE html>
<html lang="en">
<head>
<meta charset="utf-8">
<title>Kravel Construction Ltd – Business Card</title>
<link rel="stylesheet" href="https://fonts.googleapis.com/css2?family=Lato:wght@400;700;900&display=swap">
<style>
  :root {
    --page-bg: #e4e4e4;
    --card-white: #ffffff;
    --green-dark: #4a8c3f;
    --green-light: #72bf44;
    --text-light: #ffffff;
    --sketch-grey: #dcdcdc;
  }
  * { box-sizing: border-box; margin: 0; padding: 0; }
  html, body {
    width: 1200px; height: 1200px; overflow: hidden;
    background: var(--page-bg);
    font-family: "Lato", Arial, sans-serif;
  }
  .card {
    position: absolute; left: 180px;
    width: 840px; height: 480px;
    background: var(--card-white);
    overflow: hidden;
  }
  .card--front { top: 80px; }
  .card--back { top: 640px; }

  .building-sketch {
    position: absolute; left: 0; top: 20px;
    width: 350px; height: 318px;
    background: linear-gradient(100deg, var(--sketch-grey) 0%, #eeeeee 45%, rgba(255,255,255,0) 100%);
    opacity: .8;
  }
  .card--back .building-sketch { height: 306px; }

  .wordmark {
    position: absolute; left: 0; right: 0; top: 130px;
    text-align: center; color: var(--green-light);
    font-weight: 900; line-height: 1;
  }
  .wordmark__name { display: block; font-size: 78px; letter-spacing: 2px; }
  .wordmark__sub { display: block; font-size: 19px; letter-spacing: 6px; margin-top: 10px; }

  .band {
    position: absolute; left: 0; right: 0; bottom: 0;
    background: var(--green-dark);
    border-top: 5px solid var(--green-light);
    color: var(--text-light);
  }
  .card--front .band { top: 333px; }
  .card--back .band { top: 320px; }

  .contact-row {
    position: absolute; inset: 0;
    display: flex; align-items: center;
  }
  .person { position: absolute; left: 62px; top: 44px; }
  .person__name { font-size: 25px; font-weight: 700; letter-spacing: .3px; }
  .person__title { font-size: 14px; margin-top: 5px; }

  .divider {
    position: absolute; top: 45px; width: 1px; height: 56px;
    background: rgba(255,255,255,.8);
  }
  .divider--one { left: 304px; }
  .divider--two { left: 542px; }

  .contact-list { position: absolute; top: 44px; list-style: none; }
  .contact-list--phones { left: 358px; font-size: 17px; font-weight: 700; }
  .contact-list--online { left: 587px; font-size: 16px; font-weight: 700; }
  .contact-list li { display: flex; align-items: center; gap: 6px; height: 28px; }
  .contact-list svg { width: 15px; height: 15px; flex: none; }

  .services { position: absolute; left: 63px; top: 26px; right: 40px; }
  .services__heading { font-size: 16px; font-weight: 400; letter-spacing: .3px; margin-bottom: 16px; }
  .services__row { display: flex; font-size: 13.5px; height: 25px; align-items: center; }
  .services__row span + span::before {
    content: ""; display: inline-block; width: 1px; height: 16px;
    background: rgba(255,255,255,.85); vertical-align: middle;
    margin: 0 18px;
  }
</style>
</head>
<body>

<section class="card card--front">
  <div class="building-sketch" role="img" aria-label="Faint line sketch of a modern office building"></div>
  <div class="wordmark">
    <span class="wordmark__name">KRAVEL</span>
    <span class="wordmark__sub">CONSTRUCTION LTD</span>
  </div>
  <div class="band">
    <div class="person">
      <p class="person__name">TOMAS VERBELK</p>
      <p class="person__title">(Managing Director)</p>
    </div>
    <span class="divider divider--one"></span>
    <ul class="contact-list contact-list--phones">
      <li>
        <svg viewBox="0 0 16 16" fill="none" stroke="#fff" stroke-width="1.2"><circle cx="8" cy="8" r="7"/><path d="M5.5 4.5l1.5 1.5-1 1c.6 1.3 1.7 2.4 3 3l1-1 1.5 1.5-1 1.2c-2.5-.3-5-2.8-5.3-5.3z" fill="#fff" stroke="none"/></svg>
        020 5194 6381
      </li>
      <li>
        <svg viewBox="0 0 16 16" fill="none" stroke="#fff" stroke-width="1.2"><rect x="4" y="1" width="8" height="14" rx="1.5"/><line x1="7" y1="12.5" x2="9" y2="12.5"/></svg>
        07845319027
      </li>
    </ul>
    <span class="divider divider--two"></span>
    <ul class="contact-list contact-list--online">
      <li>
        <svg viewBox="0 0 16 16" fill="none" stroke="#fff" stroke-width="1.1"><circle cx="8" cy="8" r="6.5"/><ellipse cx="8" cy="8" rx="3" ry="6.5"/><line x1="1.5" y1="8" x2="14.5" y2="8"/><line x1="2.5" y1="5" x2="13.5" y2="5"/><line x1="2.5" y1="11" x2="13.5" y2="11"/></svg>
        www.kravel.co.uk
      </li>
      <li>
        <svg viewBox="0 0 16 16" fill="none" stroke="#fff" stroke-width="1.1"><rect x="1" y="3.5" width="14" height="9"/><path d="M1 3.5l7 5.5 7-5.5M1 12.5l5-4.5M15 12.5l-5-4.5"/></svg>
        tomas@kravel.co.uk
      </li>
    </ul>
  </div>
</section>

<section class="card card--back">
  <div class="building-sketch" role="img" aria-label="Faint line sketch of a modern office building"></div>
  <div class="wordmark">
    <span class="wordmark__name">KRAVEL</span>
    <span class="wordmark__sub">CONSTRUCTION LTD</span>
  </div>
  <div class="band">
    <div class="services">
      <h2 class="services__heading">SERVICES WE PROVIDE:</h2>
      <p class="services__row"><span>Kitchen Renovations</span><span>Bathroom Renovations</span><span>House Renovations</span><span>Garage Conversions</span><span>Extensions</span></p>
      <p class="services__row"><span>Loft Conversions</span><span>Conservatories</span><span>Carpentry</span><span>Tiling</span><span>Electrical</span><span>Plumbing &amp; Heating</span></p>
      <p class="services__row"><span>Bricklaying</span><span>Landscaping</span><span>Decorating</span><span>Plastering</span></p>
    </div>
  </div>
</section>

</body>
</html>
```